Disability Magazine – Cover + Full Inside Layout

About the Publication

Our magazine is a quarterly, high‑impact publication that celebrates the lives, achievements, and everyday experiences of people with disabilities. It aims to inform, inspire, and advocate for accessibility, inclusion, and empowerment across all communities.

Target Audience

Adults (18‑65) with visible or invisible disabilities
Caregivers, family members, and allies
Professionals in health, education, policy, and design fields
Advocates and NGOs focused on accessibility

Project Goals

Visually compelling cover that instantly signals the magazine’s inclusive mission.
Consistent, readable interior layout for feature articles, interviews, photo essays, and resource guides.
Design that works both in print (A4, 300 dpi) and digitally (PDF/online flipbook).

```html
<!DOCTYPE html>
<html lang="en">
<head>
<meta charset="utf-8">
<title>Reach &amp; Rise – Quarterly Magazine Spread Overview</title>
<link href="https://fonts.googleapis.com/css2?family=Montserrat:wght@200;300;400;600;700&family=Oswald:wght@400;500&family=Open+Sans:wght@400;600&display=swap" rel="stylesheet">
<style>
:root{
  --stage:#8c8c8c;
  --paper:#ffffff;
  --orange:#f9a15e;
  --orange-text:#f28a36;
  --ink:#2a2a2a;
  --body:#7a7a7a;
  --black:#0c0c0c;
}
*{margin:0;padding:0;box-sizing:border-box}
html,body{width:1200px;height:382px;overflow:hidden;background:var(--stage)}
.canvas{position:relative;width:1200px;height:382px}
.page{position:absolute;width:105px;height:148px;background:var(--paper);overflow:hidden;font-family:"Montserrat",sans-serif}
.r1{top:34.5px}.r2{top:199px}
.c1{left:24.7px}.c2{left:140.9px}.c3{left:257.1px}.c4{left:373.3px}.c5{left:489.5px}
.c6{left:605.7px}.c7{left:721.9px}.c8{left:838.1px}.c9{left:954.3px}.c10{left:1070.5px}
.abs{position:absolute}
.photo{position:absolute}
.running{position:absolute;top:4px;right:4px;font-size:1.3px;font-weight:700;letter-spacing:.1px;color:#555}
.folio{position:absolute;bottom:4px;font-size:1.2px;color:#888}
.folio.l{left:7px}.folio.r{right:7px}
.body{position:absolute;font-family:"Open Sans",sans-serif;font-size:1.6px;line-height:2.3px;color:var(--body)}
.head{position:absolute;color:var(--orange-text);font-weight:400;line-height:.92;text-transform:uppercase}
.sc{text-transform:none}
.white{color:#fff}
.orange-bg{background:var(--orange)}
</style>
</head>
<body>
<main class="canvas">

<!-- Row 1 -->
<section class="page r1 c1 cover">
  <div class="photo" role="img" aria-label="Portrait of a smiling woman in an art studio" style="inset:0;background:linear-gradient(135deg,#6b4a36 0%,#3a2a22 45%,#a07256 100%)"></div>
  <div class="abs" style="top:16px;left:6px;font-weight:700;font-size:9px;color:var(--orange);letter-spacing:-.2px">REACH &amp; RISE</div>
  <div class="abs" style="top:26px;right:6px;font-size:1.4px;color:#fff;opacity:.8">The quarterly edition</div>
  <div class="body" style="top:39px;right:5px;width:30px;color:#fff;text-align:right">Inside: voices from the community, accessible homes, tech that helps, style for every body and fresh ideas for work.</div>
  <div class="abs" style="top:80px;left:6px;font-family:'Oswald',sans-serif;font-size:8.6px;line-height:1.17;color:#fff">REDEFINING<br>STRENGTH:<br>REAL STORIES,<br>REAL VOICES,<br>REAL CHANGE.</div>
  <div class="abs" style="top:110px;right:6px;width:22px;height:22px;border-radius:50%;background:var(--orange);color:#fff;font-size:2.3px;text-align:center;padding-top:7px;line-height:1.3">QUARTERLY<br>EDITION<br><span style="font-size:1.4px">ISSUE 01 · 2025</span></div>
  <div class="body" style="bottom:10px;left:6px;width:40px;color:#fff">Empowering lives through stories, insight and advocacy.</div>
</section>

<section class="page r1 c2 contents">
  <div class="abs" style="top:10px;left:5px;font-size:2.2px;font-weight:600;color:var(--orange-text)">REACH &amp; RISE</div>
  <div class="abs" style="top:14px;left:5px;font-weight:200;font-size:12.5px;letter-spacing:1.6px;color:#444">CONTENTS</div>
  <div class="abs orange-bg" style="top:32px;left:0;width:105px;height:11px;color:#fff;font-size:1.5px;display:flex;gap:10px;padding:2px 5px">
    <span>04<br>Redefining Strength</span><span>16<br>Excerpt: You And<br>Me at Breakfast</span><span>22<br>Author spotlight:<br>Nora Ashby</span>
  </div>
  <div class="photo" role="img" aria-label="Woman with flying hair typing on a vintage typewriter" style="left:0;top:43px;width:61px;height:80px;background:linear-gradient(160deg,#bfb2a4,#6f6256 60%,#3e3833)"></div>
  <div class="abs" style="top:126px;left:8px;font-size:1.6px;color:#888">10 Young Emerging Writers</div>
  <div class="body" style="top:48px;left:63px;width:38px;font-size:1.4px;line-height:2px">
    <b>Breaking Barriers</b><br>How inclusive design is reshaping the future.<br><br><b>Everyday Brilliance</b><br>Portraits of strength and expression.<br><br><b>In Conversation With: Lena Marlowe</b><br>Advocacy, art and access.<br><br><b>Voices of Change</b><br>Readers share their stories.<br><br><b>Fashion That Fits Every Body</b><br>Adaptive style ideas.<br><br><b>Accessibility Resources</b><br>Tools worth knowing.<br><br><b>Your Rights: A Quick Overview</b>
  </div>
  <span class="folio r">REACH &amp; RISE MAGAZINE · 2</span>
</section>

<section class="page r1 c3">
  <span class="running">REACH &amp; RISE FEATURE</span>
  <div class="head" style="top:14px;left:10px;font-size:5.6px;font-weight:600">Breaking Barriers:<br>How Inclusive Design Is<br>Reshaping the Future</div>
  <div class="body" style="top:32px;left:10px;width:86px;font-size:1.3px;line-height:1.8px">A deep dive into the designers, creators and everyday advocates pushing accessibility into mainstream culture.</div>
  <div class="photo" role="img" aria-label="Hands holding a latte with foam art" style="left:10px;top:42px;width:60px;height:47px;background:linear-gradient(135deg,#8ab7bf,#e0d2bf 55%,#7c5a40)"></div>
  <div class="abs" style="left:70px;top:42px;width:28px;height:47px;background:#fde7d6;color:var(--orange-text);font-size:2.2px;padding:5px 3px;line-height:1.25">“Accessibility is not an add‑on, it’s a human right.”</div>
  <div class="body" style="top:92px;left:10px;width:86px">Inclusive design is no longer a niche practice, it is becoming a global movement. From public spaces to digital platforms, accessibility is shaping the way we think about innovation and the people it serves.</div>
  <div class="head" style="top:113px;left:10px;font-size:4px;font-weight:600">The<br>Movement<br>Gaining<br>Momentum</div>
  <div class="abs" style="top:113px;left:48px;font-size:2px;font-weight:700;color:#333">Fast Facts</div>
  <div class="body" style="top:117px;left:48px;width:48px;font-size:1.3px;line-height:2px">• 1.3 billion people worldwide live with a disability<br>• Accessibility increases usability for everyone<br>• Inclusive products lead to higher satisfaction</div>
  <span class="folio r">REACH &amp; RISE MAGAZINE · 5</span>
</section>

<section class="page r1 c4 orange-bg">
  <span class="running" style="left:4px;right:auto;color:#fff">REACH &amp; RISE FEATURE</span>
  <div class="abs" style="top:24px;left:7px;font-weight:600;font-size:8.6px;line-height:.96;color:#fff">IN<br>CONVERSATION<br>WITH:<br>LENA<br>MARLOWE</div>
  <div class="abs" style="top:81px;left:7px;width:42px;height:55px;background:#fff;padding:3px">
    <div style="font-size:1.7px;font-weight:700;color:#333">Q&amp;A: LENA MARLOWE</div>
    <div class="body" style="position:static;font-size:1.3px;line-height:1.9px;margin-top:1px">Lena is a designer and advocate whose work brings people together to rethink access in daily life.<br><br><b>WHAT STARTED YOUR PASSION FOR ACCESSIBILITY ADVOCACY?</b><br>It began at home.<br><br><b>WHAT CHANGES DO YOU HOPE TO SEE IN THE NEXT FIVE YEARS?</b><br>Access as standard.</div>
  </div>
  <div class="photo" role="img" aria-label="Smiling woman using a smartphone outdoors" style="left:49px;top:83px;width:50px;height:53px;background:linear-gradient(150deg,#d9cfc4,#a99482 50%,#5c6f7c)"></div>
  <div class="abs" style="top:64px;left:76px;width:24px;font-size:1.9px;color:#fff;line-height:1.3">“Representation isn’t optional—it’s essential.”</div>
  <span class="folio l" style="color:#fff">6 · REACH &amp; RISE MAGAZINE</span>
</section>

<section class="page r1 c5">
  <span class="running">REACH &amp; RISE FEATURE</span>
  <div class="abs" style="top:15px;left:9px;width:70px;height:28px;border:.6px solid #222;padding:7px 5px;color:var(--orange-text);font-size:3.2px;line-height:1.05">EVERYDAY BRILLIANCE:<br>PORTRAITS OF STRENGTH<br>&amp; EXPRESSION</div>
  <div class="body" style="top:51px;left:9px;width:30px;font-size:1.3px;line-height:1.9px">A visual journey highlighting the beauty, confidence and individuality of people living with visible and invisible disabilities.</div>
  <div class="photo" role="img" aria-label="Group of friends, one in a wheelchair, laughing together outdoors" style="left:40px;top:51px;width:65px;height:82px;background:linear-gradient(140deg,#cfe0ea,#8b9c8e 45%,#4a3b30)"></div>
  <div class="body" style="top:118px;left:9px;width:28px;font-size:1.3px;line-height:1.9px"><b>Caption:</b><br>Describe the person, moment, or story.<br><br><b>Photo Credit:</b><br>Photographer Name</div>
  <span class="folio r">REACH &amp; RISE MAGAZINE · 7</span>
</section>

<section class="page r1 c6">
  <span class="running" style="left:4px;right:auto">REACH &amp; RISE FEATURE</span>
  <div class="photo" role="img" aria-label="Woman in a wide-brim hat and denim jacket" style="left:55px;top:0;width:50px;height:148px;background:linear-gradient(170deg,#d8cfc5,#b7a08a 45%,#4a4a52)"></div>
  <div class="head" style="top:49px;left:7px;font-size:6.2px;font-weight:600">Style That<br>Fits Every<br>Body</div>
  <div class="body" style="top:74px;left:7px;width:45px">A magazine is a periodical publication, which can either be printed or published electronically. It is issued regularly, usually every week or every month, and it contains a variety of content.<br><br>To create your own, choose a topic that interests you. It can be anything from fashion and beauty to travel and the home. Once you have your overall theme, you can start collecting ideas.</div>
  <span class="folio l">8 · REACH &amp; RISE MAGAZINE</span>
</section>

<section class="page r1 c7">
  <span class="running">REACH &amp; RISE FEATURE</span>
  <div class="head" style="top:12px;left:10px;font-size:7.4px;font-weight:300;line-height:.86">Style Tips for<br>Practical Everyday<br>Wear</div>
  <div class="body" style="top:34px;left:10px;width:26px;font-size:1.3px;line-height:1.9px">A visual journey highlighting the beauty, confidence and individuality of people living with visible and invisible disabilities.</div>
  <div class="body" style="top:34px;left:44px;width:55px">To create your own, choose a topic that interests you. It can be anything from fashion and beauty to travel. Once you have your overall theme, you can start collecting ideas and gathering the pieces that will tell your story. Think about your readers and what they need.</div>
  <div class="photo" role="img" aria-label="Woman meditating on rocks in the desert" style="left:7px;top:64px;width:93px;height:64px;background:linear-gradient(180deg,#e9eef2,#c8b7a5 60%,#8a7360)"></div>
  <span class="folio r">REACH &amp; RISE MAGAZINE · 9</span>
</section>

<section class="page r1 c8">
  <span class="running" style="left:4px;right:auto">REACH &amp; RISE FEATURE</span>
  <div class="head" style="top:14px;left:7px;font-size:5.8px;font-weight:600">Stories From Our Readers</div>
  <div class="photo" role="img" aria-label="Portrait of a smiling man" style="left:0;top:24px;width:51px;height:33px;background:linear-gradient(135deg,#9a2e2e,#d3b29a 55%,#7a5a45)"></div>
  <div class="photo" role="img" aria-label="Portrait of a woman with curly hair" style="left:0;top:59px;width:51px;height:37px;background:linear-gradient(135deg,#e6e6e6,#8a6248 55%,#3a2a22)"></div>
  <div class="photo" role="img" aria-label="Portrait of a man in a dark shirt" style="left:0;top:98px;width:51px;height:38px;background:linear-gradient(135deg,#f0f0f0,#6d4a38 55%,#2a2020)"></div>
  <div class="abs" style="top:24px;left:55px;font-size:1.9px;font-weight:700;color:#333">Jordan P. Reyes</div>
  <div class="body" style="top:28px;left:55px;width:45px;font-size:1.3px;line-height:1.9px">Lorem ipsum shares how finding the right community changed everything, from daily routines to the confidence to speak up at work and at home.</div>
  <div class="abs" style="top:60px;left:55px;font-size:1.9px;font-weight:700;color:#333">Amara K. Velez</div>
  <div class="body" style="top:64px;left:55px;width:45px;font-size:1.3px;line-height:1.9px">A story about learning to ask for support, building new habits and discovering strength that was there all along.</div>
  <div class="abs" style="top:99px;left:55px;font-size:1.9px;font-weight:700;color:#333">Tomas R. Ellery</div>
  <div class="body" style="top:103px;left:55px;width:45px;font-size:1.3px;line-height:1.9px">How adaptive sport opened doors to friendship, travel and a brand new sense of purpose.</div>
  <span class="folio l">10 · REACH &amp; RISE MAGAZINE</span>
</section>

<section class="page r1 c9">
  <span class="running">REACH &amp; RISE FEATURE</span>
  <div class="head" style="top:12px;left:10px;font-size:7px;font-weight:300;line-height:.86">Building Inclusive<br>Workplaces</div>
  <div class="photo" role="img" aria-label="Woman walking on a Paris street with the Eiffel Tower behind" style="left:5px;top:32px;width:47px;height:68px;background:linear-gradient(180deg,#cfdbe6,#c9b8a2 55%,#6f6458)"></div>
  <div class="abs" style="top:103px;left:10px;font-size:1.3px;font-weight:600;color:#444">By Jane Doe<br>Photography by Alex Rowe</div>
  <div class="head" style="top:124px;left:10px;font-size:3.2px;font-weight:600">Romantic<br>Travel:<br>Paris,<br>France</div>
  <div class="body" style="top:103px;left:55px;width:45px">A magazine is a periodical publication that can be printed or published online. It is issued regularly and contains a variety of content. To create your own, choose a topic that interests you and start collecting ideas.</div>
  <span class="folio r">REACH &amp; RISE MAGAZINE · 11</span>
</section>

<section class="page r1 c10">
  <span class="running" style="left:4px;right:auto">REACH &amp; RISE FEATURE</span>
  <div class="photo" role="img" aria-label="Woman meditating cross-legged on a lawn" style="left:5px;top:8px;width:95px;height:61px;background:linear-gradient(180deg,#dfe8e4,#9fb78d 55%,#5f7f4a)"></div>
  <div class="head" style="top:72px;left:7px;font-size:9.5px;font-weight:400;line-height:.9">Mental Wellness<br>Matters</div>
  <div class="abs" style="top:98px;left:7px;font-size:1.3px;font-weight:600;color:#444">By Jane Doe<br>Photography by Alex Rowe</div>
  <div class="body" style="top:98px;left:30px;width:70px">A magazine is a periodical publication that can be printed or published online. It is issued regularly and contains a variety of content, from articles and stories to photographs and advertisements. Choose a topic you care about and the rest will follow.</div>
  <span class="folio l">12 · REACH &amp; RISE MAGAZINE</span>
</section>

<!-- Row 2 -->
<section class="page r2 c1">
  <span class="running">REACH &amp; RISE FEATURE</span>
  <div class="head sc" style="top:12px;left:43px;font-size:7.4px;font-weight:400;line-height:.98">Helpful<br>Organizations<br>&amp; Support<br>Networks</div>
  <div class="photo" role="img" aria-label="Caregiver helping an older woman with a walker" style="left:43px;top:43px;width:62px;height:52px;background:linear-gradient(160deg,#e6edf2,#8aa6bf 50%,#3c4d64)"></div>
  <div class="body" style="top:51px;left:7px;width:33px">A magazine is a periodical publication, which can either be printed or published electronically. It is issued regularly, usually every week or every month, and it contains a variety of content. To create your own, choose a topic that interests you and start gathering ideas.</div>
  <div class="body" style="top:100px;left:43px;width:57px">Next, think of a compelling feature for your cover story. This will be the place where readers discover what matters most in this issue, so make it count.</div>
  <span class="folio r">REACH &amp; RISE MAGAZINE · 13</span>
</section>

<section class="page r2 c2">
  <span class="running" style="left:4px;right:auto">REACH &amp; RISE FEATURE</span>
  <div class="head" style="top:22px;left:7px;font-size:8.8px;font-weight:300;line-height:.86">Daily Living<br>Tools</div>
  <div class="body" style="top:40px;left:7px;width:60px;font-size:1.3px;line-height:1.9px">A curated list of devices and apps that make routines easier, safer and more independent.</div>
  <div class="body" style="top:52px;left:7px;width:43px">A magazine is a periodical publication, which can either be printed or published electronically. It is issued regularly and contains a variety of content. To create your own, choose a topic that interests you. It can be anything from fashion and beauty to travel and the home.</div>
  <div class="photo" role="img" aria-label="Blue mug beside a note reading your daily routine matters" style="left:52px;top:51px;width:53px;height:82px;background:linear-gradient(150deg,#e9dcc8,#c9b89a 50%,#3d6f9a)"></div>
  <span class="folio l">14 · REACH &amp; RISE MAGAZINE</span>
</section>

<section class="page r2 c3">
  <span class="running">REACH &amp; RISE FEATURE</span>
  <div class="body" style="top:22px;left:10px;width:32px;font-size:1.3px;line-height:1.9px">Place a quote or caption here to introduce the photo story.</div>
  <div class="photo" role="img" aria-label="Person kneeling on a cliff above the sea" style="left:45px;top:15px;width:60px;height:26px;background:linear-gradient(180deg,#c9d9e4,#7a8fa0 60%,#5a4a3c)"></div>
  <div class="photo" role="img" aria-label="Rocky coastline with turquoise water" style="left:6px;top:49px;width:49px;height:51px;background:linear-gradient(160deg,#7fb6c9,#3d7e9a 55%,#6d6a5a)"></div>
  <div class="body" style="top:71px;left:66px;width:34px;font-size:1.3px;line-height:1.9px">Add a short caption that tells the reader where this moment was captured.</div>
  <div class="body" style="top:119px;left:24px;width:34px;font-size:1.3px;line-height:1.9px">Add a short caption about this scene.</div>
  <div class="photo" role="img" aria-label="Aerial view of waves meeting a forested shore" style="left:66px;top:88px;width:36px;height:45px;background:linear-gradient(135deg,#1f6a6a,#4fa3a0 50%,#2c4a2e)"></div>
  <span class="folio r">REACH &amp; RISE MAGAZINE · 15</span>
</section>

<section class="page r2 c4 ad">
  <div class="photo" role="img" aria-label="Coastal view of Rio de Janeiro bay and mountains" style="left:0;top:0;width:105px;height:92px;background:linear-gradient(180deg,#a9cde0,#5c8fa8 45%,#2f5a46 80%,#3d4e3c)"></div>
  <div class="abs" style="top:10px;left:10px;font-size:1.4px;color:#fff">ADVERTISEMENT</div>
  <div class="abs" style="top:58px;left:10px;font-weight:600;font-size:8px;line-height:.98;color:#fff">EXPLORE<br>RIO DE<br>JANEIRO</div>
  <div class="abs" style="top:99px;left:10px;font-size:1.8px;line-height:1.4;color:#333">RIO DE JANEIRO:<br>WHERE EVERY MOMENT<br>DANCES WITH LIFE</div>
  <div class="abs" style="top:109px;left:10px;width:40px;height:.4px;background:#555"></div>
  <div class="body" style="top:112px;left:10px;width:45px;font-size:1.3px;line-height:1.9px">Sun, samba and sea views: plan your trip with accessible stays, tours and transport, all in one place.</div>
  <div class="abs" style="top:139px;left:10px;font-size:1.4px;color:#333">WWW.WAYFARRA-TRIPS.COM</div>
  <div class="abs orange-bg" style="left:58px;top:92px;width:47px;height:56px;padding:6px 8px">
    <div style="font-weight:600;font-size:8px;line-height:.95;color:#222">30%<br>OFF</div>
    <div style="font-size:1.3px;line-height:1.9px;color:#fff;margin-top:4px">When you book your accessible holiday with Wayfarra this season.</div>
  </div>
</section>

<section class="page r2 c5">
  <span class="running">REACH &amp; RISE FEATURE</span>
  <div class="abs orange-bg" style="left:0;top:0;width:69px;height:148px"></div>
  <div class="abs" style="top:30px;left:10px;font-weight:600;font-size:8px;line-height:.95;color:#111">Innovators to<br>Watch</div>
  <div class="photo" role="img" aria-label="Young man in a red shirt looking thoughtful against a teal wall" style="left:32px;top:48px;width:73px;height:52px;background:linear-gradient(135deg,#2a7f8f,#3f94a0 55%,#d2563a)"></div>
  <div class="body" style="top:108px;left:10px;width:30px;font-size:1.3px;line-height:1.9px;color:#fff">Meet the founders, engineers and makers turning lived experience into bold new ideas for everyone.</div>
  <div class="body" style="top:57px;left:6px;width:24px;font-size:1.3px;line-height:1.9px;color:#fff">Four minds redefining access.</div>
  <span class="folio r">REACH &amp; RISE MAGAZINE · 17</span>
</section>

<section class="page r2 c6">
  <span class="running" style="left:4px;right:auto">REACH &amp; RISE FEATURE</span>
  <div class="head sc" style="top:16px;left:0;width:105px;text-align:center;font-size:7.5px;font-weight:300;line-height:.98">Tech That<br>Changes Lives</div>
  <div class="body" style="top:35px;left:15px;width:75px;text-align:center;font-size:1.3px;line-height:1.9px">From voice control to smart homes, the tools opening new possibilities every day.</div>
  <div class="photo" role="img" aria-label="Coffee mug next to a note reading gratitude changes everything" style="left:0;top:47px;width:105px;height:53px;background:linear-gradient(160deg,#c4c8cc,#6b5a6e 40%,#e8e2d8 60%,#9aa4b0)"></div>
  <div class="body" style="top:103px;left:7px;width:43px">A magazine is a periodical publication, printed or published online. It is issued regularly and contains a variety of content, from articles to photographs and ads.</div>
  <div class="body" style="top:103px;left:54px;width:45px">Next, think of a compelling feature for your cover story. Consider your readers and what they need to know this season.</div>
  <span class="folio l">18 · REACH &amp; RISE MAGAZINE</span>
</section>

<section class="page r2 c7">
  <span class="running">REACH &amp; RISE FEATURE</span>
  <div class="photo" role="img" aria-label="Cafe storefront with a coffee sign" style="left:5px;top:18px;width:47px;height:30px;background:linear-gradient(180deg,#3a3a3a,#7a5a3e 60%,#2a2a2a)"></div>
  <div class="photo" role="img" aria-label="Cinnamon roll on a plate" style="left:5px;top:50px;width:47px;height:36px;background:radial-gradient(circle at 50% 50%,#d9a56a,#ead8c0 45%,#f2eee8)"></div>
  <div class="photo" role="img" aria-label="Cozy cafe interior with pendant lamp" style="left:54px;top:18px;width:46px;height:68px;background:linear-gradient(170deg,#2f5258,#556f6b 50%,#8a6a4a)"></div>
  <div class="body" style="top:91px;left:5px;width:55px">Next, think of a compelling feature for your cover story. This will be the centrepiece of the issue. When you have chosen a topic, choose the right photos and craft the layout.</div>
  <div class="abs" style="top:91px;left:66px;width:34px;font-size:1.8px;font-weight:700;line-height:1.3;color:#222">“A PULL QUOTE IS AN IMPACTFUL QUOTE TAKEN FROM THE ARTICLE. PLACE THE QUOTE HERE.”</div>
  <span class="folio r">REACH &amp; RISE MAGAZINE · 19</span>
</section>

<section class="page r2 c8">
  <span class="running" style="left:4px;right:auto">REACH &amp; RISE FEATURE</span>
  <div class="body" style="top:14px;left:5px;width:45px">A magazine is a periodical publication, which can either be printed or published electronically. It is issued regularly, usually every week or every month, and contains articles, stories, photographs and advertisements. To create your own, choose a topic that interests you and collect your ideas before you begin to design.</div>
  <div class="body" style="top:14px;left:55px;width:45px">Next, think of a compelling feature for your cover story. When you have decided on your cover story, come up with a list of topics for your feature articles. Think about what your audience would be interested in and how to keep them reading each season.</div>
  <div class="photo" role="img" aria-label="Group of young people looking at their phones" style="left:5px;top:69px;width:95px;height:65px;background:linear-gradient(180deg,#f0f0f0,#c9c2bb 45%,#5a4a40)"></div>
  <span class="folio l">20 · REACH &amp; RISE MAGAZINE</span>
</section>

<section class="page r2 c9 ad">
  <div class="photo" role="img" aria-label="Hot air balloon over red rock formations at sunset" style="inset:0;background:linear-gradient(180deg,#5c93b8 0%,#8fb7d0 30%,#b86a3a 60%,#6d3a1e 85%,#3a2616)"></div>
  <div class="abs" style="top:10px;left:10px;font-size:1.4px;color:#fff">ADVERTISEMENT</div>
  <div class="abs" style="top:19px;left:10px;font-weight:600;font-size:8px;line-height:.98;color:#fff">EXPLORE RIO<br>DE JANEIRO</div>
  <div class="abs orange-bg" style="left:14px;top:103px;width:84px;height:18px;border-radius:9px"></div>
  <div class="abs orange-bg" style="left:6px;top:95px;width:32px;height:32px;border-radius:50%;padding-top:8px;padding-left:8px;font-weight:600;font-size:7px;line-height:.95;color:#222">30%<br>OFF</div>
  <div class="abs" style="top:106px;left:43px;width:22px;font-size:1.6px;font-weight:600;line-height:1.3;color:#222">Using WAYFARRA gives you an additional discount.</div>
  <div class="abs" style="top:105px;left:70px;width:24px;font-size:1.3px;line-height:1.4;color:#fff">Discover the landmarks and corners of the city. Book your adventure today!</div>
</section>

<section class="page r2 c10" style="background:var(--black)">
  <div class="abs" style="top:10px;left:6px;font-size:1.3px;color:#fff">DECEMBER 2025</div>
  <div class="abs" style="top:10px;right:6px;font-size:1.3px;color:#fff">ISSUE NUMBER 02</div>
  <div class="abs" style="top:26px;left:6px;font-weight:700;font-size:12px;line-height:.98;letter-spacing:-.3px;color:#fff">REACH &amp;<br>RISE</div>
  <div class="photo" role="img" aria-label="Team of colleagues working in a bright office" style="left:0;top:58px;width:70px;height:90px;background:linear-gradient(160deg,#e9eef1,#9fb0bd 50%,#3d5264)"></div>
  <div class="body" style="top:104px;left:73px;width:28px;font-size:1.2px;line-height:1.9px;color:#ddd;text-align:right">TEAMS THAT THRIVE<br>BUILDING ACCESS AT WORK<br><br>TECH THAT HELPS<br>NEW TOOLS THIS SEASON<br>PLUS READER STORIES<br><br>CAREERS · HOMES<br>TRAVEL · WELLNESS</div>
</section>

</main>
</body>
</html>
```